Business Card Design - Law Firm

We are a boutique law firm located near the beach in Manly, Australia. We have recently had a new logo designed and are revamping our business cards with the new logo.

We have recently had a business card design done for us but are not entirely happy with it. We are looking for something modern, simplistic but striking. We would like to see multiple designs.

We have attached a word document which includes our new logo and the current business card design which we are looking at moving away from.

We would like the business cards to be double sided. We would like the design to include something which we can print in gloss colour when we send it to the business card printers.

```html
<!DOCTYPE html>
<html lang="en">
<head>
<meta charset="utf-8">
<title>Harbourne &amp; Partners Lawyers – Business Card</title>
<link href="https://fonts.googleapis.com/css2?family=Montserrat:wght@400;500;600;700&display=swap" rel="stylesheet">
<style>
  :root {
    --bg: #e6e7eb;
    --card: #ffffff;
    --navy: #3b4799;
    --gold: #c4aa6a;
    --ink: #222326;
  }
  * { box-sizing: border-box; margin: 0; padding: 0; }
  html, body { width: 1200px; height: 1000px; overflow: hidden; }
  body {
    background: var(--bg);
    font-family: "Montserrat", sans-serif;
    color: var(--ink);
    position: relative;
  }
  .card {
    position: absolute;
    left: 220px;
    width: 760px;
    height: 434px;
    background: var(--card);
    border-radius: 22px;
    overflow: hidden;
    box-shadow: 0 6px 20px rgba(0,0,0,0.12);
  }
  .card--front { top: 48px; }
  .card--back { top: 518px; }

  .brand {
    display: flex;
    align-items: center;
    gap: 14px;
  }
  .brand__dot {
    width: 26px; height: 26px;
    border-radius: 50%;
    background: var(--navy);
    flex: none;
  }
  .brand__name {
    font-weight: 700;
    color: var(--ink);
    letter-spacing: 1.5px;
    line-height: 1.25;
  }

  .card--front .brand {
    position: absolute;
    left: 0; right: 0; top: 160px;
    justify-content: center;
  }
  .card--front .brand__name { font-size: 30px; }
  .front__web {
    position: absolute;
    left: 0; right: 0; top: 300px;
    text-align: center;
    font-size: 17px;
    font-weight: 500;
    letter-spacing: 0.5px;
  }

  .card--back .brand {
    position: absolute;
    left: 40px; top: 110px;
    width: 290px;
  }
  .card--back .brand__name { font-size: 21px; }
  .divider {
    position: absolute;
    left: 355px; top: 60px;
    width: 2px; height: 200px;
    background: var(--navy);
  }
  .contact {
    position: absolute;
    left: 385px; top: 58px;
  }
  .contact__name {
    font-size: 28px;
    font-weight: 700;
    color: var(--navy);
    text-transform: uppercase;
    letter-spacing: 0.5px;
  }
  .contact__role {
    font-size: 17px;
    font-weight: 600;
    color: var(--gold);
    text-transform: uppercase;
    letter-spacing: 1.5px;
    margin-top: 2px;
  }
  .contact__address {
    font-size: 16px;
    line-height: 1.35;
    margin-top: 14px;
    font-style: normal;
  }
  .contact__list { list-style: none; margin-top: 12px; }
  .contact__item {
    display: flex; align-items: center; gap: 10px;
    font-size: 16px; line-height: 1.7;
  }
  .contact__icon { width: 20px; height: 20px; flex: none; }

  .footer-rule {
    position: absolute;
    left: 0; right: 0; bottom: 62px;
    height: 6px;
    background: var(--gold);
  }
  .footer-band {
    position: absolute;
    left: 0; right: 0; bottom: 0;
    height: 50px;
    background: var(--navy);
  }
</style>
</head>
<body>

<section class="card card--front" aria-label="Card front">
  <div class="brand">
    <span class="brand__dot"></span>
    <span class="brand__name">Harbourne &amp; Partners Lawyers</span>
  </div>
  <p class="front__web">www.harbourneandpartners.com.au</p>
</section>

<section class="card card--back" aria-label="Card back">
  <div class="brand">
    <span class="brand__dot"></span>
    <span class="brand__name">Harbourne &amp; Partners Lawyers</span>
  </div>

  <div class="divider"></div>

  <div class="contact">
    <h1 class="contact__name">Nora Whitfield</h1>
    <p class="contact__role">Practice Manager</p>
    <address class="contact__address">Suite 4, 12 Tidewater Lane<br>Seacliff NSW 2099</address>
    <ul class="contact__list">
      <li class="contact__item">
        <svg class="contact__icon" viewBox="0 0 20 20"><circle cx="10" cy="10" r="10" fill="var(--gold)"/><path d="M7,5 L9,7.5 L8,9 C8.8,10.6 9.6,11.4 11,12 L12.5,11 L15,13 L13.5,15 C10,14.6 5.6,10.4 5,6.5 Z" fill="#fff"/></svg>
        (02) 5550 1234
      </li>
      <li class="contact__item">
        <svg class="contact__icon" viewBox="0 0 20 20"><circle cx="10" cy="10" r="10" fill="var(--gold)"/><rect x="5" y="6.5" width="10" height="7" fill="#fff"/><path d="M5,6.5 L10,10.5 L15,6.5" fill="none" stroke="var(--gold)" stroke-width="1"/></svg>
        nora.whitfield@coastlaw.com.au
      </li>
      <li class="contact__item">
        <svg class="contact__icon" viewBox="0 0 20 20"><circle cx="10" cy="10" r="10" fill="var(--gold)"/><g fill="none" stroke="#fff" stroke-width="1.1"><circle cx="10" cy="10" r="5"/><ellipse cx="10" cy="10" rx="2.2" ry="5"/><line x1="5" y1="10" x2="15" y2="10"/></g></svg>
        www.harbourneandpartners.com.au
      </li>
    </ul>
  </div>

  <div class="footer-rule"></div>
  <div class="footer-band"></div>
</section>

</body>
</html>
```